Business Card Design

I would like a new business card design for an accounting firm that specializes in resolving clients tax problems. I want the card to give the impression that we are not your typical stodgy accounting firm, but at the same time we will get the job done.
Industry/Entity Type
Business
Contact Information for Business Card
Dorian T Welsby
Certified Public Accountant
38-27 52nd Street
Sunnyside, NY 11287
Tel: (718) 555-0142
Fax: (888) 555-0199
e-mail: dtwthecpa@ledgerpost.com
website: harborfilingreliefexperts.com

```html
<!DOCTYPE html>
<html lang="en">
<head>
<meta charset="utf-8">
<title>Dorian T Welsby, CPA – Business Card</title>
<link rel="stylesheet" href="https://fonts.googleapis.com/css2?family=Arimo:wght@400;700&display=swap">
<style>
  :root {
    --backdrop: #2c2c2c;
    --card-white: #f4f4f4;
    --card-shade: #e6e6e6;
    --navy: #1c3f78;
    --band-blue: #1b4178;
    --gold: #f7c51c;
    --band-text: #ffffff;
  }
  * { box-sizing: border-box; margin: 0; padding: 0; }
  html, body {
    width: 1200px;
    height: 1000px;
    overflow: hidden;
    background: var(--backdrop);
    font-family: "Arimo", Arial, sans-serif;
  }
  .card {
    position: absolute;
    left: 160px;
    top: 248px;
    width: 880px;
    height: 503px;
    border-radius: 24px;
    overflow: hidden;
    background: radial-gradient(ellipse at 35% 30%, #ffffff 0%, var(--card-white) 55%, var(--card-shade) 100%);
  }
  .divider {
    position: absolute;
    left: 432px;
    top: 30px;
    width: 2px;
    height: 300px;
    background: linear-gradient(to bottom, rgba(247,197,28,0) 0%, var(--gold) 30%, var(--gold) 70%, rgba(247,197,28,0) 100%);
  }
  .wordmark {
    position: absolute;
    left: 44px;
    top: 118px;
    display: flex;
    align-items: center;
    gap: 14px;
    color: var(--navy);
    font-weight: 700;
    font-size: 30px;
    letter-spacing: 2px;
  }
  .wordmark-square {
    width: 18px;
    height: 18px;
    background: var(--gold);
  }
  .holder {
    position: absolute;
    right: 66px;
    top: 74px;
    color: var(--navy);
    font-size: 24px;
    letter-spacing: 0.5px;
  }
  .holder .credential {
    font-size: 12px;
    vertical-align: 8px;
    margin-left: 4px;
  }
  .contact-list {
    position: absolute;
    right: 44px;
    top: 158px;
    list-style: none;
    color: var(--navy);
    font-size: 16px;
    text-align: right;
  }
  .contact-list li {
    display: flex;
    justify-content: flex-end;
    align-items: center;
    gap: 8px;
    margin-bottom: 8px;
  }
  .contact-list .address { line-height: 1.1; font-size: 15px; }
  .contact-list svg { width: 22px; height: 22px; flex: none; }
  .gold-rule {
    position: absolute;
    left: 0;
    right: 0;
    top: 358px;
    height: 9px;
    background: var(--gold);
  }
  .band {
    position: absolute;
    left: 0;
    right: 0;
    top: 367px;
    bottom: 0;
    background: var(--band-blue);
  }
  .website {
    position: absolute;
    left: 0;
    right: 0;
    top: 36px;
    text-align: center;
    padding-left: 120px;
    color: var(--band-text);
    font-size: 20px;
    letter-spacing: 0.3px;
  }
</style>
</head>
<body>
  <article class="card">
    <div class="divider"></div>

    <div class="wordmark">
      <span class="wordmark-square"></span>
      <span class="wordmark-name">DORIAN T. WELSBY</span>
    </div>

    <h1 class="holder">Dorian T Welsby,<span class="credential">CPA</span></h1>

    <ul class="contact-list">
      <li>
        <span>(718) 555-0142</span>
        <svg viewBox="0 0 24 24" fill="none" stroke="#1c3f78" stroke-width="1.8" aria-label="Phone">
          <circle cx="12" cy="12" r="10"/>
          <path d="M8.5 7.5c-.8.8-.8 2.6.8 4.8 1.6 2.2 3.6 3.6 5 3.6.8 0 1.4-.5 1.6-1l-1.9-1.6-1.1.8c-1-.5-2.1-1.6-2.6-2.6l.8-1.1L9.5 7.3z" fill="#1c3f78" stroke="none"/>
        </svg>
      </li>
      <li>
        <span>(888) 555-0199</span>
        <svg viewBox="0 0 24 24" fill="#1c3f78" aria-label="Fax">
          <rect x="7" y="3" width="10" height="6"/>
          <rect x="3" y="9" width="18" height="9" rx="1.5"/>
          <rect x="7" y="14" width="10" height="7" fill="#ffffff" stroke="#1c3f78" stroke-width="1.5"/>
        </svg>
      </li>
      <li>
        <span>dtwthecpa@ledgerpost.com</span>
        <svg viewBox="0 0 24 24" fill="none" stroke="#1c3f78" stroke-width="1.6" aria-label="Email">
          <rect x="2.5" y="5.5" width="19" height="13"/>
          <path d="M2.5 5.5l9.5 8 9.5-8M2.5 18.5l7-6.5M21.5 18.5l-7-6.5"/>
        </svg>
      </li>
      <li>
        <span class="address">38-27 52nd Street<br>Sunnyside, NY 11287</span>
        <svg viewBox="0 0 24 24" fill="#1c3f78" aria-label="Address">
          <path d="M12 2a6.5 6.5 0 0 0-6.5 6.5C5.5 13.5 12 21 12 21s6.5-7.5 6.5-12.5A6.5 6.5 0 0 0 12 2zm0 9a2.5 2.5 0 1 1 0-5 2.5 2.5 0 0 1 0 5z"/>
        </svg>
      </li>
    </ul>

    <div class="gold-rule"></div>
    <footer class="band">
      <p class="website">www.harborfilingreliefexperts.com</p>
    </footer>
  </article>
</body>
</html>
```